wine label design

i'm a fine wine store based in new zealand which buys quality bulk wine and bottles it, passing on the significant savings onto the customer. i require a brand name and design which is cool/ sharp and contempory. the wines will be all still wines, there won't be any sparkling wines under this brand. i've used brand names like harbourlight wine company for previous designs/label but want something more edgier. we thought about a brand name 'sky above the vines' or 'harbourlight wine co' but couldn't get a design to match the title of brand, if you have any thoughts on this send thru your design. take into account color they have to be bold as i am printing these thru a digital printer. the label is a wrap around design, the dimensions are approximately 80 or 90 mm high and 210 mm wide. have a look at these links, i think they have some x-factor to them: http://www.marlowvale.example/store/product_images/p/855/velora__34476_zoom.jpg: OR

http://static3.cellarfinder.example/images/labels/35/24/ember-in-the-fog-shiraz-petite-sirah-south-australia-10203524.jpg: OR

http://www.bottlebarn.example/ui/productimages/25223/25223_w240.jpg: OR

http://www.vintrail.example/images/viewWinery.php?pic=238291

Take into account i have to be able put a wine desription on the back label, barcode and a few technical details required by law. on the front label all i require is space to put the grape variety, area and vintage. i need the grape type to really stand out.
Updates

Reason: hi, the designs coming thru look good, just need a little more changes, also please read thru the brief, there are a few things i have noted such as label size etc etc

Target Market(s)

am after a label the cool/edgy/contempoary that appeals to the educated well off customer that willing to give something new a go by the look of the label that is cool and edgy.

Industry/Entity Type

Harbourlight

Requirements
Must have
• bold bold bold, it must stand out on the shelf
Nice to have
• a title/brand name that links what i'm doing, from what i'm doing the name 'harbourlight wine co' is probably best suited.
Should not have
• basic boring artwork and small text, the bigger the text the better

```html
<!DOCTYPE html>
<html lang="en">
<head>
<meta charset="utf-8">
<title>Harbourlight Wine Co. — Cabernet Sauvignon Wrap Label</title>
<link rel="stylesheet" href="https://fonts.googleapis.com/css2?family=Caladea:wght@400;700&display=swap">
<style>
  :root {
    --page: #ffffff;
    --label: #000000;
    --ink: #ffffff;
    --vintage-yellow: #e8e81c;
    --brand-green: #c5d42b;
    --detail-green: #8dc63f;
    --alc-green: #bccb2e;
    --panel-cream: #f6e7da;
  }
  html, body {
    margin: 0;
    padding: 0;
    width: 1200px;
    height: 900px;
    overflow: hidden;
    background: var(--page);
  }
  .canvas {
    position: relative;
    width: 1200px;
    height: 900px;
  }
  .wrap-label {
    position: absolute;
    left: 75px;
    top: 232px;
    width: 1047px;
    height: 433px;
    overflow: hidden;
    background: var(--label);
    font-family: "Caladea", Georgia, serif;
    color: var(--ink);
  }
  .back-copy {
    position: absolute;
    left: 30px;
    top: 45px;
    width: 200px;
    font-size: 11px;
    line-height: 15px;
  }
  .back-copy p { margin: 0 0 14px; }
  .barcode-panel {
    position: absolute;
    left: 28px;
    top: 354px;
    width: 195px;
    height: 69px;
    border-radius: 8px;
    background: var(--panel-cream);
  }
  .varietal {
    position: absolute;
    left: 232px;
    top: 38px;
    width: 280px;
    margin: 0;
    text-align: center;
    color: var(--vintage-yellow);
    font-weight: 700;
  }
  .varietal .vintage {
    display: block;
    font-size: 28px;
    line-height: 30px;
  }
  .varietal .grape {
    display: block;
    font-size: 21px;
    line-height: 24px;
  }
  .brand-mark {
    position: absolute;
    left: 480px;
    top: 53px;
    width: 270px;
    height: 270px;
  }
  .brand-name {
    position: absolute;
    left: 282px;
    top: 342px;
    margin: 0;
    font-size: 56px;
    line-height: 60px;
    font-weight: 700;
    white-space: nowrap;
    color: var(--brand-green);
    transform-origin: 0 100%;
    transform: rotate(-29deg);
  }
  .legal-line {
    position: absolute;
    top: 403px;
    margin: 0;
    font-size: 14px;
    line-height: 16px;
    white-space: nowrap;
    color: var(--detail-green);
  }
  .legal-line.alcohol { left: 270px; color: var(--alc-green); }
  .legal-line.origin { left: 451px; }
  .legal-line.volume { left: 720px; color: var(--alc-green); }
  .legal-line.bottler { left: 810px; }
  .side-copy {
    position: absolute;
    left: 810px;
    top: 41px;
    width: 195px;
    font-size: 11.5px;
    line-height: 16.5px;
  }
  .side-copy p { margin: 0 0 16px; }
</style>
</head>
<body>
<div class="canvas">
  <section class="wrap-label">
    <div class="back-copy">
      <p>Itecerum harumendi occum que ni cum, ommo doluptatur audist facesciatium quae velibusam si volut labo. Voluptas aditionsent.</p>
      <p>Rumet reritiur, quis nonsequam, torep eror ratur, omnihil inimet est eum re di t re opturia ndande aut reperum, qui b ea di undae perest ut unt que nimpor a ccat licae verum ?</p>
      <p>Maximagnat pliquuntus audaectius ne stis quatinctis ea nus et accus et ut odipienis res volupientor sollit, voluptae non nus eicium culpa sus.</p>
    </div>
    <div class="barcode-panel" aria-label="Space for barcode"></div>

    <h1 class="varietal">
      <span class="vintage">2008</span>
      <span class="grape">Cabernet Sauvignon</span>
    </h1>

    <svg class="brand-mark" viewBox="0 0 270 270" aria-hidden="true">
      <circle cx="135" cy="135" r="128" fill="none" stroke="#ffffff" stroke-width="4"/>
    </svg>
    <p class="brand-name">Harbourlight</p>

    <p class="legal-line alcohol">14% Alc./Vol</p>
    <p class="legal-line origin">Product of New Zealand</p>
    <p class="legal-line volume">750 ml.</p>
    <p class="legal-line bottler">Bottled by Harbourlight Wine Co.</p>

    <div class="side-copy">
      <p>Itecerum harumendi occum que ni cum, ommo doluptatur audist facesciatium quae velibusam si volut labo. Voluptas aditionsent</p>
      <p>Itecerum harumendi occum que ni cum, ommo doluptatur audist facesciatium quae velibusam si volut labo. Voluptas aditionsent</p>
      <p>Itecerum harumendi occum que ni cum, ommo doluptatur audist facesciatium quae velibusam si volut labo. Voluptas aditionsent</p>
    </div>
  </section>
</div>
</body>
</html>
```